Ridgewell Stonecraft Construction Needs business card

Hey we are in need of business card designs. I have upload our logo as a guideline, but free feel to run with it or come up with something unique.
Pls have fun with it and be creative. the name says it all!
i will give some directions after i see a few entries..
Logo source file has been uploaded..
Hey because of the logo is so colourful already.
Can we have a few submissions with less colour.
Also we are looking for clever/hidden/descriptive business card.

```html
<!DOCTYPE html>
<html lang="en">
<head>
<meta charset="utf-8">
<title>Ridgewell Stonecraft Construction – Business Card</title>
<link rel="stylesheet" href="https://fonts.googleapis.com/css2?family=Montserrat:wght@700&family=Questrial&display=swap">
<style>
  :root {
    --page-bg: #e9ebe9;
    --card-bg: #ffffff;
    --ink: #1e1e1e;
    --brand-grey: #7b7c7e;
    --accent-red: #e3212b;
    --accent-blue: #1c7fc6;
  }
  * { margin: 0; padding: 0; box-sizing: border-box; }
  html, body {
    width: 1200px; height: 1200px; overflow: hidden;
    background: var(--page-bg);
  }
  .canvas { position: relative; width: 1200px; height: 1200px; }
  .card {
    position: absolute; left: 212px; width: 800px; height: 445px;
    background: var(--card-bg);
  }
  .card--front { top: 130px; }
  .card--back { top: 641px; }

  .brand {
    position: absolute;
    display: flex; align-items: center; gap: 16px;
    color: var(--brand-grey);
    font-family: "Montserrat", sans-serif; font-weight: 700;
    text-transform: uppercase; line-height: 1.1;
  }
  .brand__mark {
    width: 44px; height: 44px; background: var(--accent-blue); flex: none;
  }
  .brand__name { font-size: 30px; letter-spacing: 0.5px; }
  .brand__name span { display: block; }
  .brand__sub { font-size: 14px; letter-spacing: 2px; margin-top: 4px; }

  .card--front .brand { left: 0; right: 0; top: 180px; justify-content: center; }
  .card--back .brand { left: 78px; top: 224px; }
  .card--back .brand__name { font-size: 27px; }

  .contact {
    position: absolute; left: 443px; top: 122px;
    font-family: "Questrial", sans-serif; color: var(--ink);
  }
  .contact__person { font-size: 14px; letter-spacing: 3px; }
  .contact__name { font-family: "Montserrat", sans-serif; font-weight: 700; }
  .contact__dash { margin: 0 6px; }
  .contact__role { color: var(--accent-red); }
  .contact__address {
    margin-top: 30px; font-size: 14px; letter-spacing: 2.6px; line-height: 21px;
    text-transform: uppercase;
  }
  .contact__list { list-style: none; margin-top: 22px; }
  .contact__list li {
    display: flex; align-items: center; height: 25px;
    font-size: 14px; letter-spacing: 2.4px;
  }
  .contact__list svg { width: 16px; height: 16px; margin-right: 20px; flex: none; }
</style>
</head>
<body>
<main class="canvas">

  <section class="card card--front" aria-label="Card front">
    <div class="brand">
      <div class="brand__mark"></div>
      <div>
        <div class="brand__name"><span>Ridgewell Stonecraft</span></div>
        <div class="brand__sub">Construction</div>
      </div>
    </div>
  </section>

  <section class="card card--back" aria-label="Card back">
    <div class="brand">
      <div class="brand__mark"></div>
      <div>
        <div class="brand__name"><span>Ridgewell</span><span>Stonecraft</span></div>
        <div class="brand__sub">Construction</div>
      </div>
    </div>

    <div class="contact">
      <p class="contact__person">
        <span class="contact__name">MARLA OKONJO</span><span class="contact__dash">-</span><span class="contact__role">DIRECTOR</span>
      </p>
      <p class="contact__address">Shop 2, 118-122 Harbour<br>Road Lindfield East</p>
      <ul class="contact__list">
        <li>
          <svg viewBox="0 0 16 16" fill="none" stroke="var(--accent-red)" stroke-width="1.6"><path d="M2 6c0-2 3-3 6-3s6 1 6 3l-2 1-1-2H5L4 7z" fill="var(--accent-red)"/><path d="M4 8h8l1 5H3z"/><circle cx="8" cy="10.5" r="1"/></svg>
          5713 2841
        </li>
        <li>
          <svg viewBox="0 0 16 16" fill="none" stroke="var(--accent-red)" stroke-width="1.5"><rect x="4" y="1.5" width="8" height="4"/><rect x="1.5" y="5.5" width="13" height="6" rx="1"/><rect x="4" y="9.5" width="8" height="5"/></svg>
          5713 2869
        </li>
        <li>
          <svg viewBox="0 0 16 16" fill="none" stroke="var(--accent-red)" stroke-width="1.5"><rect x="1" y="3.5" width="14" height="9"/><path d="M1 3.5l7 5 7-5M1 12.5l5-4.5M15 12.5l-5-4.5"/></svg>
          marla@ridgewellstone.com
        </li>
        <li>
          <svg viewBox="0 0 16 16" fill="none" stroke="var(--accent-red)" stroke-width="1.4"><circle cx="7.5" cy="7.5" r="6"/><ellipse cx="7.5" cy="7.5" rx="2.6" ry="6"/><path d="M1.5 7.5h12M2.5 4.5h10M2.5 10.5h10"/><path d="M10 10l5 2-2 1-1 2z" fill="var(--accent-red)" stroke="none"/></svg>
          www.ridgewellstone.com
        </li>
      </ul>
    </div>
  </section>

</main>
</body>
</html>
```